new business card, with new logo. Looking for full design

I would like to have a graphic designer/artist create a high standard, premium business logo and business card design that I can either use to print on my own or have printed through them as well. Also, would be nice if I could customize with new employee names and info afterwards. Also, though I don't have a logo, something that matches the theme here https://veridanstrategy.com/ as well as incorporates the letter "M" is what I am currently thinking. Thanks!

Target Market(s)

High end corporate executives

Industry/Entity Type

Economics

Contact Information for Business Card

Dr. Tomas Ruelle-Brandt
Principal Advisor
TRB@VeridanStrategy.com
other contact/website details from here: https://veridanstrategy.com/

Logo Text

Veridan Strategy Group

```html
<!DOCTYPE html>
<html lang="en">
<head>
<meta charset="utf-8">
<title>Veridan Strategy Group – Business Card</title>
<link rel="stylesheet" href="https://fonts.googleapis.com/css2?family=Cinzel:wght@500&family=Tinos&display=swap">
<style>
  :root {
    --backdrop: #3b3b3d;
    --paper: #ffffff;
    --onyx: #0c0c0c;
    --ink: #111111;
    --rose: #c48f86;
    --display: "Cinzel", serif;
    --body: "Tinos", serif;
  }
  * { margin: 0; padding: 0; box-sizing: border-box; }
  html, body { width: 1200px; height: 900px; overflow: hidden; }
  body {
    background: var(--backdrop);
    position: relative;
    font-family: var(--body);
  }
  .card {
    position: absolute;
    left: 240px;
    width: 720px;
    height: 411px;
    border-radius: 26px;
    overflow: hidden;
  }
  .card--front { top: 28px; background: var(--paper); }
  .card--back  { top: 461px; background: var(--onyx); }

  .brand { position: absolute; display: flex; align-items: center; gap: 16px; }
  .brand__square { width: 64px; height: 64px; border: 2px solid var(--rose); flex: none; }
  .brand__name {
    font-family: var(--display);
    font-weight: 500;
    font-size: 27px;
    letter-spacing: 3px;
    text-transform: uppercase;
    white-space: nowrap;
  }
  .card--front .brand { left: 46px; top: 38px; }
  .card--front .brand__name { color: var(--ink); }
  .card--back .brand { left: 50%; top: 50%; transform: translate(-50%, -50%); }
  .card--back .brand__name { color: var(--paper); }

  .person { position: absolute; left: 46px; top: 176px; }
  .person__name {
    font-family: var(--display);
    font-weight: 500;
    font-size: 22px;
    letter-spacing: 1px;
    color: var(--ink);
  }
  .person__title {
    font-family: var(--display);
    font-weight: 500;
    font-size: 16px;
    letter-spacing: 1.5px;
    color: var(--rose);
    margin-top: 2px;
  }
  .divider {
    position: absolute;
    left: 300px; right: 40px; top: 222px;
    height: 1.5px;
    background: var(--ink);
  }
  .contacts { position: absolute; left: 46px; top: 248px; list-style: none; }
  .contacts li {
    display: flex; align-items: center; gap: 10px;
    font-size: 16px; color: var(--ink);
    margin-bottom: 8px;
  }
  .contacts svg { width: 15px; height: 15px; flex: none; }
  .address {
    position: absolute; right: 40px; bottom: 44px;
    display: flex; align-items: center; gap: 14px;
  }
  .address__text { text-align: right; font-size: 19px; line-height: 1.35; color: var(--ink); }
  .address svg { width: 18px; height: 24px; }
</style>
</head>
<body>

<section class="card card--front" aria-label="Business card front">
  <div class="brand">
    <span class="brand__square"></span>
    <span class="brand__name">Veridan Strategy Group</span>
  </div>

  <div class="person">
    <p class="person__name">DR. TOMAS RUELLE-BRANDT</p>
    <p class="person__title">MANAGING DIRECTOR</p>
  </div>
  <div class="divider"></div>

  <ul class="contacts">
    <li>
      <svg viewBox="0 0 16 16" aria-hidden="true"><path d="M4 1.5l2.2 3-1.3 1.6a8 8 0 0 0 5 5l1.6-1.3 3 2.2-1.2 2.3C8 14 2 8 2.2 2.7z" fill="var(--rose)"/></svg>
      0742-5518-3096
    </li>
    <li>
      <svg viewBox="0 0 16 16" aria-hidden="true"><rect x="1" y="3" width="14" height="10" fill="none" stroke="var(--rose)" stroke-width="1.6"/><path d="M1 3l7 6 7-6" fill="none" stroke="var(--rose)" stroke-width="1.6"/></svg>
      info@VeridanStrategy.com
    </li>
    <li>
      <svg viewBox="0 0 16 16" aria-hidden="true"><g fill="none" stroke="var(--rose)" stroke-width="1.3"><circle cx="8" cy="8" r="6.5"/><ellipse cx="8" cy="8" rx="2.8" ry="6.5"/><path d="M1.5 8h13M2.5 4.8h11M2.5 11.2h11"/></g></svg>
      www.veridanstrategy.com
    </li>
  </ul>

  <div class="address">
    <p class="address__text">2210 L St NW, Suite 410<br>Washington, DC 20037</p>
    <svg viewBox="0 0 18 24" aria-hidden="true"><path d="M9 1a7.5 7.5 0 0 0-7.5 7.5C1.5 14 9 23 9 23s7.5-9 7.5-14.5A7.5 7.5 0 0 0 9 1z" fill="var(--rose)"/><circle cx="9" cy="8.5" r="3" fill="var(--paper)"/></svg>
  </div>
</section>

<section class="card card--back" aria-label="Business card back">
  <div class="brand">
    <span class="brand__square"></span>
    <span class="brand__name">Veridan Strategy Group</span>
  </div>
</section>

</body>
</html>
```